Layout for new page on existing website

We have an existing website (www.brightloomworks.org) and need a new page designing to promote a new product.
The new page needs to be consistent with the existing website look and feel (www.brightloomworks.org) but current persistent elements on the standard page design can be moved/removed from the page to accommodate a new layout necessary for getting all the content laid out in a logical user friendly way.
The content required for the page is attached along with a wireframe mock up that may help understand the expectation, however the wireframe was just created to help me work out what was needed on the page and the layout can be different. A key element is the quality of the design of each of the artifacts (e.g. the panel the embedded video needs to go in, icons etc) and a clear display of the information.
Updates
The website that the new page needs to fit into is www.brightloomworks.org, i will also added the company logo to the brief.
Our Corporate Colours
- Green: #A2FF00
- Cream: #FFFF99
- Yellow: #FFE900
- Grey: #534741
Industry/Entity Type
Product
Look and feel
Each slider illustrates characteristics of the customer's brand and the style your logo design should communicate.

```html
<!DOCTYPE html>
<html lang="en">
<head>
<meta charset="utf-8">
<title>Course Admin – Benefits | Brightloom Works</title>
<link href="https://fonts.googleapis.com/css2?family=Ubuntu:wght@400;500;700&display=swap" rel="stylesheet">
<style>
  :root {
    --page-bg: #544841;
    --column-shade: #3f3530;
    --panel-bg: #3d3532;
    --green: #A2FF00;
    --yellow: #FFE900;
    --cream: #FFFF99;
    --text: #ffffff;
    --label: #f2eee9;
    --footer-text: #9a8d82;
    --field: #ffffff;
  }
  * { box-sizing: border-box; margin: 0; padding: 0; }
  html, body {
    width: 1200px; height: 883px; overflow: hidden;
    background: var(--page-bg);
    font-family: "Ubuntu", "Trebuchet MS", sans-serif;
  }
  .page { position: relative; width: 1200px; height: 883px; }
  .page::before, .page::after {
    content: ""; position: absolute; top: 0; width: 14px; height: 760px;
    background: linear-gradient(to bottom, var(--column-shade) 70%, rgba(63,53,48,0));
  }
  .page::before { left: 120px; box-shadow: 4px 0 8px rgba(0,0,0,.25); }
  .page::after { left: 1067px; box-shadow: -4px 0 8px rgba(0,0,0,.25); }

  .section-title {
    position: absolute; left: 156px; top: 16px;
    font-size: 24px; font-weight: 700; color: var(--green); letter-spacing: -0.3px;
  }
  .panel { position: absolute; left: 154px; width: 892px; background: var(--panel-bg); }
  .benefits { top: 57px; height: 425px; padding: 22px 20px 0 28px; }
  .benefit-list { list-style: none; }
  .benefit-list li {
    position: relative; padding-left: 14px; margin-bottom: 8.7px;
    font-size: 13px; font-weight: 500; line-height: 20.4px; color: var(--text);
  }
  .benefit-list li::before {
    content: ""; position: absolute; left: 0; top: 5px;
    border-left: 7px solid var(--yellow);
    border-top: 5px solid transparent; border-bottom: 5px solid transparent;
  }

  .quote-title {
    position: absolute; left: 170px; top: 502px;
    font-size: 24px; font-weight: 700; color: var(--green); letter-spacing: -0.3px;
  }
  .quote-title .highlight { color: var(--yellow); }
  .quote-form { top: 542px; height: 228px; }
  .field-label {
    position: absolute; left: 16px; font-size: 16.5px; color: var(--label);
  }
  .field-input {
    position: absolute; left: 133px; width: 261px; height: 23px;
    background: var(--field); border: none;
  }
  .send-button {
    position: absolute; left: 133px; top: 167px; width: 94px; height: 36px;
    background: var(--cream); border: none;
    font-family: "Ubuntu", "Trebuchet MS", sans-serif;
    font-size: 19px; font-weight: 700; color: #111;
  }

  .site-footer {
    position: absolute; left: 0; width: 1200px; top: 833px;
    text-align: center; font-size: 12px; color: var(--footer-text);
    padding-left: 148px;
  }
  .footer-brand {
    position: absolute; left: 1000px; top: 822px;
    display: flex; align-items: center; gap: 5px;
    font-size: 11px; font-weight: 500; color: var(--cream);
  }
  .footer-brand .dot { width: 12px; height: 12px; border-radius: 50%; background: var(--cream); }
</style>
</head>
<body>
<main class="page">
  <h2 class="section-title">BENEFITS</h2>
  <section class="panel benefits">
    <ul class="benefit-list">
      <li>Live Availability – Availability on course place availability to prevent overbooking Customers can search for Courses and Book Online with immediate confirmation</li>
      <li>Automated confirmation emails</li>
      <li>Be available for business 24/7 and take orders anytime! Customers can book when it’s most convenient for them – be it early morning, late evening or weekend</li>
      <li>No fielding phone calls, no wading through paper registrations. Attendees book on your website, there and then No more trips to the bank, take immediate and secure payments online</li>
      <li>Automated confirmation emails so reducing the time need communicating with candidates</li>
      <li>Boost course bookings and reduce administrative time and costs</li>
      <li>Course Admin is Web based meaning you can access your course information from anywhere at any time.</li>
      <li>System is very intuitive and easy to use.</li>
      <li>Lighten your workload</li>
      <li>Upload and manage offline bookings through the admin dashboard</li>
      <li>Keep your attendees organized all the way up to the course date and beyond</li>
    </ul>
  </section>

  <h2 class="quote-title">Contact us now and Get your <span class="highlight">FREE NO OBLIGATION QUOTE</span></h2>
  <form class="panel quote-form">
    <label class="field-label" style="top:28px">Name</label>
    <input class="field-input" style="top:20px" type="text" aria-label="Name">
    <label class="field-label" style="top:64px">Company</label>
    <input class="field-input" style="top:56px" type="text" aria-label="Company">
    <label class="field-label" style="top:100px">Email</label>
    <input class="field-input" style="top:92px" type="email" aria-label="Email">
    <label class="field-label" style="top:137px">Telephone</label>
    <input class="field-input" style="top:129px" type="tel" aria-label="Telephone">
    <button class="send-button" type="button">SEND</button>
  </form>

  <footer class="site-footer">| ©2010 Brightloom Works, All Rights Reserved | Disclaimer |</footer>
  <div class="footer-brand"><span class="dot"></span>Brightloom Works</div>
</main>
</body>
</html>
```